Forensic Psychology and Polygraph Needs Clever Catchy Logo

There's a massive trade show coming up and we are looking to debut a new, clever logo for our business cards. We are a private practice that offers psychological evaluations, therapeutic counseling, and polygraphing. Our website is kelvora.net (to get a better idea of the color scheme) and instead of the nature/cuddly image that other psychology organizations like to go for, we are interested in cultivating a business, strength, and professional image.
Attached are some popular logos and designs to get those creative juices flowing! I would like to avoid the brain/psi logo as this has been to death so bonus points definitely for originality.
Target Market(s)
governmental agencies, third party mental health providers, individual private pay clients
Industry/Entity Type
Mental Health
Contact Information for Business Card
One one side will be the logo and company name while on the back will be contact information and provider details (name, position, etc)
Look and feel
Each slider illustrates characteristics of the customer's brand and the style your logo design should communicate.

```html
<!DOCTYPE html>
<html lang="en">
<head>
<meta charset="utf-8">
<title>Halbrook &amp; Associates – Business Card</title>
<link rel="stylesheet" href="https://fonts.googleapis.com/css2?family=Roboto+Condensed:wght@500&family=Arimo:wght@400;700&display=swap">
<style>
  :root {
    --backdrop: #545050;
    --teal: #3fb9bd;
    --teal-dark: #3aa6aa;
    --plum: #554a55;
    --stone: #8c8c8c;
    --silver: #b9b9b9;
    --paper-top: #ffffff;
    --paper-bottom: #efefef;
    --ink: #4a4a4a;
    --ink-soft: #5d5d5d;
    --white: #ffffff;
  }
  * { box-sizing: border-box; margin: 0; padding: 0; }
  html, body {
    width: 1073px; height: 1200px; overflow: hidden;
    background: var(--backdrop);
    font-family: "Arimo", Arial, sans-serif;
  }
  .canvas { position: relative; width: 1073px; height: 1200px; }

  .brand-variant {
    position: absolute; top: 62px;
    display: flex; align-items: center; gap: 14px;
    font-family: "Roboto Condensed", "Arial Narrow", sans-serif;
    font-weight: 500; font-size: 36px; white-space: nowrap;
  }
  .brand-variant .dot { width: 30px; height: 30px; border-radius: 50%; }
  .brand-variant--light { left: 70px; color: var(--white); }
  .brand-variant--light .dot { background: var(--silver); }
  .brand-variant--teal { left: 628px; color: var(--teal); }
  .brand-variant--teal .dot { background: var(--teal-dark); }

  .card {
    position: absolute; left: 153px; width: 785px;
    border-radius: 30px; overflow: hidden;
  }
  .card--front {
    top: 192px; height: 449px; background: var(--teal);
    display: flex; align-items: center; justify-content: center;
  }
  .front-brand {
    display: flex; align-items: center; gap: 22px;
    font-family: "Roboto Condensed", "Arial Narrow", sans-serif;
    font-weight: 500; font-size: 50px; color: var(--plum); white-space: nowrap;
  }
  .front-brand .dot { width: 46px; height: 46px; border-radius: 50%; background: var(--plum); }

  .card--back {
    top: 707px; height: 450px;
    background: linear-gradient(180deg, var(--paper-top), var(--paper-bottom) 60%);
  }
  .holder { position: absolute; left: 65px; top: 72px; }
  .holder__name { font-size: 25px; color: var(--ink); letter-spacing: .5px; }
  .holder__name b { font-weight: 700; }
  .holder__role { margin-top: 14px; font-size: 19px; color: var(--ink); }
  .address {
    position: absolute; left: 63px; top: 176px;
    font-size: 19.5px; line-height: 28px; color: var(--ink-soft);
  }

  .contact-strip {
    position: absolute; left: 0; bottom: 0; width: 100%; height: 161px;
    display: flex;
  }
  .contact { position: relative; height: 100%; display: flex; align-items: flex-end; justify-content: center; }
  .contact--mail { width: 261px; background: var(--teal); }
  .contact--phone { width: 271px; background: var(--stone); }
  .contact--web { flex: 1; background: var(--teal); }
  .contact__tab { position: absolute; top: 0; left: 50%; transform: translateX(-50%); }
  .contact__text { margin-bottom: 42px; font-size: 19px; color: var(--ink); white-space: nowrap; }
  .contact--phone .contact__text { color: var(--white); font-size: 20px; margin-bottom: 50px; }
</style>
</head>
<body>
<main class="canvas">
  <div class="brand-variant brand-variant--light"><span class="dot"></span>Halbrook &amp; Associates</div>
  <div class="brand-variant brand-variant--teal"><span class="dot"></span>Halbrook &amp; Associates</div>

  <section class="card card--front">
    <div class="front-brand"><span class="dot"></span>Halbrook &amp; Associates</div>
  </section>

  <section class="card card--back">
    <div class="holder">
      <p class="holder__name">YOUR <b>FAMILIE</b></p>
      <p class="holder__role">Geschäftsinhaber</p>
    </div>
    <p class="address">
      Halbrook &amp; Associates Psychological Services, PLLC<br>
      2280 W. Larkspur Ave. Suites 230 and 238 Salem,<br>
      Oregon 97301
    </p>

    <div class="contact-strip">
      <div class="contact contact--mail">
        <svg class="contact__tab" width="124" height="62" viewBox="0 0 124 62" aria-hidden="true">
          <polygon points="2,30 62,60 122,30 62,46" fill="#9a9a9a"/>
          <polygon points="2,0 122,0 122,26 62,46 2,26" fill="#fff"/>
          <rect x="51" y="12" width="22" height="15" fill="#555"/>
          <polyline points="51,12 62,21 73,12" fill="none" stroke="#fff" stroke-width="1.6"/>
        </svg>
        <span class="contact__text">frontdesk@kelvora.net</span>
      </div>
      <div class="contact contact--phone">
        <svg class="contact__tab" width="124" height="62" viewBox="0 0 124 62" aria-hidden="true">
          <polygon points="2,30 62,60 122,30 62,46" fill="#6e6e6e"/>
          <polygon points="2,0 122,0 122,26 62,46 2,26" fill="#fff"/>
          <path d="M55 9c2-1 4 3 4 4s-2 2-2 3 3 5 5 6 2-1 3-1 4 2 3 4-3 3-5 2c-5-2-9-7-10-12-1-3 0-5 2-6z" fill="#555"/>
        </svg>
        <span class="contact__text">555.014.2287</span>
      </div>
      <div class="contact contact--web">
        <svg class="contact__tab" width="124" height="62" viewBox="0 0 124 62" aria-hidden="true">
          <polygon points="2,30 62,60 122,30 62,46" fill="#9a9a9a"/>
          <polygon points="2,0 122,0 122,26 62,46 2,26" fill="#fff"/>
          <circle cx="62" cy="20" r="11" fill="#555"/>
          <ellipse cx="62" cy="20" rx="5" ry="11" fill="none" stroke="#fff" stroke-width="1.2"/>
          <line x1="51" y1="20" x2="73" y2="20" stroke="#fff" stroke-width="1.2"/>
        </svg>
        <span class="contact__text">www.kelvora.net</span>
      </div>
    </div>
  </section>
</main>
</body>
</html>
```